Vehicle Design and Graphics for our company vehicles

Looking to create a 'look' for our vehicles that is simple, flashy and recognizable. Our primary colors are Red and White. We use Silver (Chrome), Grey and Black as accent colors.
Attached:
Photo # 1: is a concept that we like.
Photo # 2: Is the actual vehicle we use.
Photo # 3: Our Logo (Side of Vehicle and Front Hood
Photo # 4: Logo for rear of vehicle
Photo # 5: Exclamation Point from our logo
Photo # 6: Lock from logo
Photo # 7: Button from logo (lock)
Vehicle is a 2015 Tovrel Quenta cargo van - No windows in the cargo area or back doors.
BRISK WARD SIGNAL is a 40 year old company that focuses on Security, Fire and Life Safety of both Homes and Businesses. Our primary products / services are Burglar / Intrusion Alarms, Fire Alarms, Access Control Systems, Video Camera Systems and 24-hour monitoring service.
It Company
Other font styles liked:
- Our logo was created from the ethnocentric font.

```html
<!DOCTYPE html>
<html lang="en">
<head>
<meta charset="utf-8">
<title>Brisk Ward Signal – Rear Van Graphics</title>
<link rel="stylesheet" href="https://fonts.googleapis.com/css2?family=Oswald:wght@600;700&display=swap">
<style>
  :root {
    --brand-red: #ec2027;
    --text-red: #b3161f;
    --deep-red: #7a0d12;
    --tail-red: #c81d2c;
    --tail-pink: #e0147a;
    --amber: #ff9a1f;
    --body-white: #ffffff;
    --outline: #9a9a9a;
    --bumper: #4a4a4c;
    --bumper-dark: #2e2e30;
    --tire: #3a3a3c;
    --chrome: #e4e4e6;
    --page: #ffffff;
  }
  html, body {
    margin: 0;
    padding: 0;
    width: 1200px;
    height: 1142px;
    overflow: hidden;
    background: var(--page);
  }
  .van-rear {
    display: block;
    width: 1200px;
    height: 1142px;
  }
  .brand-name {
    font-family: "Oswald", sans-serif;
    font-weight: 700;
    font-size: 74px;
    fill: var(--text-red);
    letter-spacing: 2px;
  }
  .service-item {
    font-family: "Oswald", sans-serif;
    font-weight: 700;
    font-size: 23px;
    fill: var(--text-red);
    paint-order: stroke;
    stroke: #6b0b10;
    stroke-width: 0.6px;
  }
  .service-bullet { fill: #222; }
  .contact-line {
    font-family: "Oswald", sans-serif;
    font-weight: 700;
    fill: var(--body-white);
    text-anchor: middle;
    letter-spacing: 1.5px;
  }
  .contact-shadow { fill: var(--deep-red); }
  .contact-phone { font-size: 56px; letter-spacing: 3px; }
  .contact-web { font-size: 58px; }
</style>
</head>
<body>
<svg class="van-rear" viewBox="0 0 1010 960" preserveAspectRatio="none" xmlns="http://www.w3.org/2000/svg">
  <defs>
    <linearGradient id="tailGlow" x1="0" x2="1" y1="0" y2="0">
      <stop offset="0" stop-color="var(--tail-red)"/>
      <stop offset="0.55" stop-color="var(--tail-pink)"/>
      <stop offset="1" stop-color="var(--tail-red)"/>
    </linearGradient>
    <linearGradient id="handleGrey" x1="0" x2="0" y1="0" y2="1">
      <stop offset="0" stop-color="#f4f4f5"/>
      <stop offset="1" stop-color="#cfcfd2"/>
    </linearGradient>
  </defs>

  <!-- tires -->
  <g class="tires">
    <rect x="22" y="820" width="138" height="135" rx="12" fill="var(--tire)" stroke="#1f1f20" stroke-width="3"/>
    <rect x="850" y="820" width="138" height="135" rx="12" fill="var(--tire)" stroke="#1f1f20" stroke-width="3"/>
  </g>

  <!-- mirrors -->
  <g class="mirrors">
    <rect x="0" y="240" width="50" height="80" rx="14" fill="var(--chrome)" stroke="var(--outline)" stroke-width="2"/>
    <rect x="960" y="240" width="50" height="80" rx="14" fill="var(--chrome)" stroke="var(--outline)" stroke-width="2"/>
  </g>

  <!-- body -->
  <path class="van-body" d="M20 140 Q30 40 120 28 L890 28 Q980 40 990 140 L1000 570 L10 570 Z"
        fill="var(--body-white)" stroke="var(--outline)" stroke-width="2"/>
  <line class="door-seam" x1="505" y1="42" x2="505" y2="570" stroke="#c8c8ca" stroke-width="1.5"/>
  <line x1="78" y1="60" x2="78" y2="570" stroke="#e2e2e4" stroke-width="1.5"/>
  <line x1="932" y1="60" x2="932" y2="570" stroke="#e2e2e4" stroke-width="1.5"/>

  <!-- roof brake light -->
  <rect x="437" y="14" width="138" height="28" rx="3" fill="#2a2a2c"/>
  <rect x="447" y="24" width="118" height="14" fill="var(--tail-pink)"/>

  <!-- tail lights -->
  <g class="tail-lights">
    <path d="M27 190 L110 190 L110 360 L22 360 Z" fill="url(#tailGlow)"/>
    <rect x="35" y="268" width="53" height="28" fill="var(--amber)"/>
    <path d="M900 190 L983 190 L988 360 L900 360 Z" fill="url(#tailGlow)"/>
    <rect x="922" y="268" width="53" height="28" fill="var(--amber)"/>
  </g>

  <!-- brand name -->
  <g class="brand">
    <circle cx="150" cy="187" r="18" fill="var(--text-red)"/>
    <text class="brand-name" x="530" y="212" text-anchor="middle">BRISK WARD SIGNAL</text>
  </g>

  <!-- services -->
  <g class="services services-left">
    <circle class="service-bullet" cx="142" cy="302" r="4"/>
    <text class="service-item" x="153" y="311">Security</text>
    <circle class="service-bullet" cx="142" cy="337" r="4"/>
    <text class="service-item" x="153" y="346">Fire / Life Safety</text>
    <circle class="service-bullet" cx="142" cy="371" r="4"/>
    <text class="service-item" x="153" y="380">Burglar / Intrusion Alarms</text>
    <circle class="service-bullet" cx="142" cy="406" r="4"/>
    <text class="service-item" x="153" y="415">Fire Alarms</text>
  </g>
  <g class="services services-right">
    <circle class="service-bullet" cx="552" cy="302" r="4"/>
    <text class="service-item" x="563" y="311">Access Control Systems</text>
    <circle class="service-bullet" cx="552" cy="337" r="4"/>
    <text class="service-item" x="563" y="346">Video Camera Systems</text>
    <circle class="service-bullet" cx="552" cy="371" r="4"/>
    <text class="service-item" x="563" y="380">24-Hour Monitoring Service</text>
    <circle class="service-bullet" cx="552" cy="406" r="4"/>
    <text class="service-item" x="563" y="415">Commercial / Residential</text>
  </g>

  <!-- door handle plate -->
  <g class="door-handle">
    <rect x="540" y="462" width="250" height="106" rx="6" fill="#fafafa" stroke="var(--outline)" stroke-width="1.5"/>
    <rect x="548" y="472" width="38" height="68" rx="5" fill="#3c3c3e"/>
    <rect x="596" y="470" width="176" height="90" rx="6" fill="#dcdcdf" stroke="#a8a8ab" stroke-width="1"/>
    <rect x="603" y="476" width="162" height="76" rx="5" fill="url(#handleGrey)"/>
  </g>

  <!-- red band -->
  <path class="contact-band" d="M10 570 L1000 570 L1002 690 Q1000 728 960 728 L50 728 Q8 728 8 690 Z" fill="var(--brand-red)"/>

  <!-- contact -->
  <g class="contact">
    <text class="contact-line contact-phone contact-shadow" x="509" y="627">555 210-4878</text>
    <text class="contact-line contact-phone" x="505" y="623">555 210-4878</text>
    <text class="contact-line contact-web contact-shadow" x="509" y="692">www.briskwardsignal.com</text>
    <text class="contact-line contact-web" x="505" y="688">www.briskwardsignal.com</text>
  </g>

  <!-- bumper -->
  <g class="bumper">
    <rect x="10" y="728" width="990" height="110" rx="16" fill="var(--bumper)" stroke="var(--bumper-dark)" stroke-width="2"/>
    <path d="M30 762 L300 762 Q330 762 345 780 L365 800 Q375 810 395 810 L615 810 Q635 810 645 800 L665 780 Q680 762 710 762 L980 762"
          fill="none" stroke="var(--bumper-dark)" stroke-width="3"/>
    <path d="M30 778 L296 778 Q318 778 332 792 L352 812 Q366 826 392 826 L618 826 Q644 826 658 812 L678 792 Q692 778 714 778 L980 778"
          fill="none" stroke="#5c5c5e" stroke-width="2"/>
  </g>
</svg>
</body>
</html>
```